Anchorwell Giving - New Website Designed

I need a site that looks like this http://www.lumenhavenfund.org for boat donations. So please replace the cars with boats.

```html
<!DOCTYPE html>
<html lang="en">
<head>
<meta charset="utf-8">
<title>Anchorwell Giving – Donate Your Boat</title>
<link href="https://fonts.googleapis.com/css2?family=Open+Sans:wght@400;600;700;800&display=swap" rel="stylesheet">
<style>
:root{
  --navy:#0d2a7a;
  --navy-deep:#0a1f5c;
  --red:#9e1712;
  --red-dark:#7d100c;
  --gold:#c9a55a;
  --ink:#2b2b2b;
  --muted:#555;
  --line:#d5d5d5;
  --paper:#ffffff;
}
*{box-sizing:border-box;margin:0;padding:0}
html,body{width:1200px;height:2679px;overflow:hidden}
body{font-family:"Open Sans",Arial,sans-serif;color:var(--ink);background:var(--paper);position:relative}
.abs{position:absolute}

/* header */
.topband{left:0;top:0;width:1200px;height:157px;background:linear-gradient(100deg,#0b1a44 0%,#1c2f6a 30%,#5a1e2c 65%,#3a1320 100%)}
.brand{left:214px;top:60px;font-weight:800;font-size:30px;color:var(--gold);letter-spacing:.5px;display:flex;align-items:center;gap:14px}
.brand-dot{width:22px;height:22px;border-radius:50%;background:var(--gold)}
.nav{left:0;top:157px;width:1200px;height:46px;background:linear-gradient(90deg,var(--navy-deep),#1b3a9a 60%,var(--navy))}
.nav ul{list-style:none;display:flex;gap:50px;position:absolute;left:177px;top:12px}
.nav li{color:#fff;font-weight:700;font-size:15px}
.hero{left:0;top:203px;width:1200px;height:377px;background:linear-gradient(180deg,#8a7d6e 0%,#d8a560 45%,#6b5a4a 80%,#3a3a3a 100%)}

/* donate panel */
.panel{left:795px;top:0;width:373px;height:580px;background:var(--red)}
.call{left:815px;top:40px;display:flex;align-items:center;gap:14px;color:#fff}
.call-icon{width:66px;height:66px;border:3px solid #fff;border-radius:50%;display:flex;align-items:center;justify-content:center;flex:none}
.call-text b{display:block;font-size:19px;font-weight:700;line-height:1.1}
.call-text strong{display:block;font-size:29px;font-weight:800;line-height:1.1}
.call-text small{display:block;font-size:12px;font-weight:700}
.online{left:780px;top:157px;width:388px;height:46px;background:#fff;color:var(--red);font-weight:800;font-size:19px;text-align:center;line-height:46px}
.online-badge{left:960px;top:138px;width:24px;height:24px;border-radius:50%;background:var(--red);border:2px solid #fff}
.form{left:812px;top:222px;width:322px}
.form h3{color:#fff;font-size:16px;font-weight:700;text-align:center;margin-bottom:10px}
.row{display:flex;gap:6px;margin-bottom:8px}
.field{flex:1;height:30px;background:#fff;border-radius:3px;font-size:12px;font-weight:600;color:#333;padding:0 8px;line-height:30px;position:relative}
.field.select::after{content:"";position:absolute;right:0;top:0;width:26px;height:30px;background:#ddd;border-left:1px solid #bbb}
.field.select::before{content:"";position:absolute;right:8px;top:12px;border:5px solid transparent;border-top:6px solid #555;z-index:1}
.btn-donate{margin-top:10px;width:157px;height:40px;background:var(--navy);color:#fff;font-weight:700;font-size:15px;text-align:center;line-height:40px;border-radius:3px}

/* banner */
.strip{left:0;top:580px;width:1200px;height:233px;background:linear-gradient(180deg,#eaeaea,#d9d9d9)}
.strip-flag{left:0;top:580px;width:540px;height:233px;background:linear-gradient(120deg,#0b2470,#1d3fa0 50%,#0d2a7a);clip-path:polygon(0 0,440px 0,540px 233px,0 233px)}
.strip-title{left:58px;top:628px;color:#fff;font-weight:800}
.strip-title .l1{font-size:27px}
.strip-title .l2{font-size:58px;color:var(--gold);line-height:1.1;letter-spacing:1px}
.strip-title .l3{font-size:29px}
.perks{left:553px;top:640px;display:flex}
.perk{width:153px;text-align:center;color:var(--red);font-size:13px;font-weight:700;line-height:1.3}
.perk svg{display:block;margin:0 auto 14px}

/* sections */
.sec-title{width:1200px;text-align:center;font-size:30px;font-weight:800;color:var(--navy)}
.sec-title span{color:var(--red)}
.rule{height:1px;background:var(--line)}
.step{display:flex;gap:16px;align-items:flex-start}
.step svg{flex:none}
.step h4{color:var(--navy);font-size:15px;font-weight:800;margin:18px 0 12px;line-height:1.3}
.step p{font-size:14px;color:var(--muted);line-height:1.45;font-weight:600}

.why{left:0;top:1157px;width:1200px;height:415px;background:linear-gradient(100deg,#f2f2f2 0%,#e4e4e4 45%,#c9c3bb 70%,#ece8e4 100%)}
.why-list{left:140px;top:1290px;list-style:none}
.why-list li{display:flex;align-items:center;gap:16px;font-size:14px;color:#333;height:33px}
.why-list b{font-weight:700}
.bullet{width:24px;height:24px;border-radius:50%;background:var(--red);display:flex;align-items:center;justify-content:center;flex:none}

.faq-photo{left:80px;top:1705px;width:520px;height:425px;background:linear-gradient(170deg,#c23b3b 0%,#e9e3e0 35%,#2b3e7e 60%,#7d7a6b 85%,#5a5550 100%)}
.faq{left:634px;top:1705px;width:486px}
.q{border:1px solid #ccc;border-radius:10px;height:38px;margin-bottom:10px;padding:0 14px;display:flex;align-items:center;justify-content:space-between;font-size:15px;font-weight:700;color:var(--navy-deep)}
.q.open{height:auto;display:block;padding:10px 14px 14px}
.q.open .qh{display:flex;justify-content:space-between;margin-bottom:6px}
.q.open p{font-size:13px;color:var(--muted);font-weight:400;line-height:1.5}

/* footer */
.footer{left:0;top:2232px;width:1200px;height:408px;background:linear-gradient(110deg,#0b2577,#1c3f9e 40%,#0d2a7a 70%,#112f85)}
.tab{left:357px;top:2188px;width:483px;height:70px;background:#0d2a7a;border-radius:40px 40px 0 0}
.foot-brand{left:0;top:2226px;width:1200px;text-align:center;font-weight:800;font-size:24px;color:var(--gold)}
.fcol{color:#fff}
.fcol h5{font-size:14px;font-weight:700;padding-bottom:10px;border-bottom:1px solid rgba(255,255,255,.4);margin-bottom:18px}
.fcol p{font-size:12px;line-height:1.55;font-weight:600}
.fcol ul{list-style:none;font-size:13px;line-height:1.4;font-weight:600}
.badge{border-radius:4px;background:#e8eef7;margin-bottom:14px}
.foot-call{left:779px;top:2357px;width:352px;height:150px;border:2px solid #fff;border-radius:8px;display:flex;align-items:center;gap:14px;padding-left:22px;color:#fff}
.copy{left:0;top:2640px;width:1200px;height:39px;background:#fff;text-align:center;line-height:39px;font-size:11px;font-weight:700;color:#333}
</style>
</head>
<body>

<header>
  <div class="abs topband"></div>
  <div class="abs brand"><span class="brand-dot"></span>ANCHORWELL GIVING</div>
  <nav class="abs nav"><ul><li>HOW TO DONATE</li><li>WHY DONATE</li><li>FAQ</li><li>ABOUT</li></ul></nav>
  <div class="abs hero" role="img" aria-label="Photo of a soldier in camouflage hugging a child holding a small flag, with a harbour of sailboats at sunset behind"></div>

  <aside class="abs panel"></aside>
  <div class="abs call">
    <div class="call-icon"><svg width="32" height="32" viewBox="0 0 24 24"><path fill="#fff" d="M6.6 10.8a15.1 15.1 0 006.6 6.6l2.2-2.2c.3-.3.7-.4 1-.2 1.1.4 2.3.6 3.6.6.6 0 1 .4 1 1V20c0 .6-.4 1-1 1A17 17 0 013 4c0-.6.4-1 1-1h3.5c.6 0 1 .4 1 1 0 1.3.2 2.5.6 3.6.1.3 0 .7-.2 1z"/></svg></div>
    <div class="call-text"><b>CALL TODAY TO DONATE</b><strong>1-800-555-0142</strong><small>Live Operators Available - 7 Days A Week</small></div>
  </div>
  <div class="abs online">DONATE YOUR BOATS ONLINE</div>
  <div class="abs online-badge"></div>
  <form class="abs form">
    <h3>Full Tax Deduction - Running or Not</h3>
    <div class="row"><div class="field">First Name</div><div class="field">Last Name</div></div>
    <div class="row"><div class="field">Daytime Phone</div><div class="field">Email</div></div>
    <div class="row"><div class="field">Pickup Address</div></div>
    <div class="row"><div class="field">Pickup City</div></div>
    <div class="row"><div class="field select">Pickup State</div><div class="field">Zip Code</div></div>
    <div class="row"><div class="field select">Choose Year</div><div class="field select">Choose Make</div></div>
    <div class="row"><div class="field">Vehicle Model</div></div>
    <div class="btn-donate">DONATE NOW</div>
  </form>
</header>

<section>
  <div class="abs strip"></div>
  <div class="abs strip-flag" role="img" aria-label="Waving flag band in deep blue"></div>
  <div class="abs strip-title"><div class="l1">DONATE YOUR BOATS TO</div><div class="l2">VETERANS</div><div class="l3">MAKE A DIFFERENCE</div></div>
  <div class="abs perks">
    <div class="perk"><svg width="60" height="60" viewBox="0 0 60 60"><circle cx="30" cy="30" r="25" fill="none" stroke="#0d2a7a" stroke-width="4"/><path d="M18 30l9 9 18-20" fill="none" stroke="#0d2a7a" stroke-width="5"/></svg>You have<br>no costs</div>
    <div class="perk"><svg width="60" height="60" viewBox="0 0 60 60"><path d="M6 38h48l-8 10H14z" fill="#0d2a7a"/><path d="M18 36V26h18l8 10z" fill="#0d2a7a"/></svg>Free pickup,<br>running or not</div>
    <div class="perk"><svg width="60" height="60" viewBox="0 0 60 60"><rect x="14" y="6" width="32" height="48" fill="none" stroke="#0d2a7a" stroke-width="3"/><path d="M20 42h20M20 48h20" stroke="#0d2a7a" stroke-width="3"/><text x="30" y="32" font-size="18" font-weight="700" fill="#0d2a7a" text-anchor="middle" font-family="Open Sans,sans-serif">$</text></svg>We issue you an<br>IRS tax receipt</div>
    <div class="perk"><svg width="60" height="60" viewBox="0 0 60 60"><rect x="22" y="8" width="30" height="42" fill="none" stroke="#0d2a7a" stroke-width="3"/><circle cx="20" cy="34" r="10" fill="#fff" stroke="#0d2a7a" stroke-width="3"/><path d="M13 41l-7 9" stroke="#0d2a7a" stroke-width="4"/><path d="M30 18h16M34 26h12" stroke="#0d2a7a" stroke-width="3"/></svg>We take care of<br>all paperwork.</div>
  </div>
</section>

<section>
  <div class="abs rule" style="left:357px;top:891px;width:90px"></div>
  <h2 class="abs sec-title" style="left:0;top:870px">HOW TO <span>DONATE</span></h2>
  <div class="abs rule" style="left:753px;top:891px;width:90px"></div>

  <div class="abs step" style="left:62px;top:950px;width:345px">
    <svg width="80" height="90" viewBox="0 0 80 90"><rect x="20" y="4" width="48" height="12" fill="#9e1712"/><rect x="30" y="22" width="38" height="12" fill="#9e1712"/><rect x="30" y="40" width="38" height="12" fill="#9e1712"/><path d="M8 30v40l10-8 8 16 6-3-8-15h12z" fill="#9e1712"/></svg>
    <div><h4>CALL US AT 1-800-555-0142 OR FILL OUT THE ONLINE FORM</h4><p>Donating your boat is easy and donation is accepted nationwide.</p></div>
  </div>
  <div class="abs step" style="left:446px;top:950px;width:345px">
    <svg width="80" height="70" viewBox="0 0 80 70"><path d="M4 38h72l-10 16H14z" fill="#9e1712"/><path d="M24 36V20h26l12 16z" fill="#9e1712"/><rect x="32" y="10" width="4" height="10" fill="#9e1712"/></svg>
    <div><h4>WE PICK UP THE BOAT</h4><p>Any boats is accepted and we will arrange to pick up your boat when it is most convenient for you.</p></div>
  </div>
  <div class="abs step" style="left:848px;top:950px;width:300px">
    <svg width="76" height="90" viewBox="0 0 80 90"><rect x="22" y="6" width="44" height="64" fill="none" stroke="#9e1712" stroke-width="3"/><rect x="12" y="16" width="44" height="64" fill="#fff" stroke="#9e1712" stroke-width="3"/><text x="34" y="50" font-size="24" font-weight="700" fill="#9e1712" text-anchor="middle" font-family="Open Sans,sans-serif">$</text><path d="M20 64h28M20 70h28" stroke="#9e1712" stroke-width="3"/></svg>
    <div><h4>TAX WRITE-OFF</h4><p>Once the boat donation is complete, you will receive your tax deductable boat donation receipt.</p></div>
  </div>
</section>

<section>
  <div class="abs why" role="img" aria-label="Faded photo of soldiers raising a large flag at sunset"></div>
  <h2 class="abs sec-title" style="left:0;top:1210px">WHY DONATE <span>YOUR BOATS TO US</span></h2>
  <ul class="abs why-list">
    <li><span class="bullet"><svg width="12" height="12" viewBox="0 0 12 12"><path d="M2 6h7M6 2l4 4-4 4" stroke="#fff" stroke-width="2" fill="none"/></svg></span><span><b>Top-Rated Charity &amp; IRS 501(c)3 Approved :</b> Free 24/7 Pickup with No DMV Hassles.</span></li>
    <li><span class="bullet"><svg width="12" height="12" viewBox="0 0 12 12"><path d="M2 6h7M6 2l4 4-4 4" stroke="#fff" stroke-width="2" fill="none"/></svg></span><span><b>Free Local Towing :</b> We will pick up your boat donation, running or not, when it's most convenient.</span></li>
    <li><span class="bullet"><svg width="12" height="12" viewBox="0 0 12 12"><path d="M2 6h7M6 2l4 4-4 4" stroke="#fff" stroke-width="2" fill="none"/></svg></span><span><b>All Boats Accepted :</b> We take your car regardless of its condition or registration status.</span></li>
    <li><span class="bullet"><svg width="12" height="12" viewBox="0 0 12 12"><path d="M2 6h7M6 2l4 4-4 4" stroke="#fff" stroke-width="2" fill="none"/></svg></span><span><b>Income Tax Deduction :</b> We issue you an IRS tax receipt &amp; offer the largest resale network to get you the highest tax write-off possible.</span></li>
    <li><span class="bullet"><svg width="12" height="12" viewBox="0 0 12 12"><path d="M2 6h7M6 2l4 4-4 4" stroke="#fff" stroke-width="2" fill="none"/></svg></span><span><b>No Paperwork Hassles :</b> We take any boat and handle everything: DMV, Smog and IRS paperwork.</span></li>
    <li><span class="bullet"><svg width="12" height="12" viewBox="0 0 12 12"><path d="M2 6h7M6 2l4 4-4 4" stroke="#fff" stroke-width="2" fill="none"/></svg></span><span><b>Boat donations help fund programs :</b> And benefit Harborline Service Fund. An IRS 501(c)3 nonprofit organization.</span></li>
    <li><span class="bullet"><svg width="12" height="12" viewBox="0 0 12 12"><path d="M2 6h7M6 2l4 4-4 4" stroke="#fff" stroke-width="2" fill="none"/></svg></span><span><b>Schedule a Free Pickup :</b> Complete the form and a representative will call you to arrange a convenient time to pickup your boat.</span></li>
  </ul>
</section>

<section>
  <div class="abs rule" style="left:290px;top:1648px;width:58px"></div>
  <h2 class="abs sec-title" style="left:0;top:1626px">FREQUENTLY ASKED <span>QUESTIONS</span></h2>
  <div class="abs rule" style="left:852px;top:1648px;width:95px"></div>
  <div class="abs faq-photo" role="img" aria-label="Flag overlaid on a photo of marching soldiers' boots"></div>
  <div class="abs faq">
    <div class="q">What types of boats can be donated?<span>⌄</span></div>
    <div class="q open"><div class="qh">What paperwork do I need to donate my boat?<span>⌃</span></div><p>All you need is a title, free of all liens. We will request some general information from you at the time of donation such as, the year, make, and model of the boat, as well as its general mechanical condition. We accept all boats, running or non-running.</p></div>
    <div class="q">Is my donated boat tax -deductible?<span>⌄</span></div>
    <div class="q">What if the boat is not registered in my name?<span>⌄</span></div>
    <div class="q">How much will I receive as a tax deduction for my boat?<span>⌄</span></div>
    <div class="q">When will I receive my tax receipt?<span>⌄</span></div>
    <div class="q">How do I schedule a pick up?<span>⌄</span></div>
  </div>
</section>

<footer>
  <div class="abs footer" role="img" aria-label="Deep blue waving flag background"></div>
  <div class="abs tab"></div>
  <div class="abs foot-brand">ANCHORWELL GIVING</div>
  <div class="abs fcol" style="left:73px;top:2357px;width:240px"><h5>ABOUT ANCHORWELL GIVING</h5><p>Lorem ipsum dolor sit amet, consectetuer adipiscing elit, sed diam nonummy nibheu ismod tincidunt ut laoreet dolore magna aliquam erat volutpat. Ut wisi enim ad mini veniam, quis nostrud exerci tation ullamcor per suscipit lobortis nisl ut aliquip ex ea co modo consequat.</p></div>
  <div class="abs fcol" style="left:380px;top:2357px;width:150px"><h5>NAVIGATION</h5><ul><li>HOW TO DONATE</li><li>WHY DONATE</li><li>FAQ</li><li>ABOUT</li></ul></div>
  <div class="abs fcol" style="left:555px;top:2357px;width:160px"><h5>SAFE &amp; SECURE</h5>
    <div class="badge" style="width:160px;height:50px"></div>
    <div class="badge" style="width:120px;height:40px"></div>
    <div class="badge" style="width:66px;height:42px;border-radius:50%"></div>
  </div>
  <div class="abs foot-call">
    <div class="call-icon"><svg width="32" height="32" viewBox="0 0 24 24"><path fill="#fff" d="M6.6 10.8a15.1 15.1 0 006.6 6.6l2.2-2.2c.3-.3.7-.4 1-.2 1.1.4 2.3.6 3.6.6.6 0 1 .4 1 1V20c0 .6-.4 1-1 1A17 17 0 013 4c0-.6.4-1 1-1h3.5c.6 0 1 .4 1 1 0 1.3.2 2.5.6 3.6.1.3 0 .7-.2 1z"/></svg></div>
    <div class="call-text"><b>CALL TODAY TO DONATE</b><strong>1-800-555-0142</strong><small>Live Operators Available - 7 Days A Week</small></div>
  </div>
  <div class="abs copy">COPYRIGHT © 2017 ANCHORWELL GIVING. PRIVACY POLICY I TERMS &amp; CONDITIONS. ALL RIGHTS RESERVED.</div>
</footer>

</body>
</html>
```